Dynamic Tradeshow Banner Size: 33"W x 72"H

Dynamic design for a stand-up banner - limited text (only pertinent company information). Need design and concept for HVAC equipment faded into the background with possibly work area included.
Website Address: MobileBreezeandVolt.com
Telephone Number: 888-417-2806
Additional text: 24/7 Rapid Response

Target Market(s)

Banner for Tradeshow. Target Customers: Hotels, hospitals, facility managers, factories, etc... Any potential to need portable air or power generation when theirs is inoperable.

Industry/Entity Type

Hvac

Font styles to use
Sans Serif

Colors

Designer to choose colors to be used in the design.

Requirements
Must have
• Dynamic design with pictures included... Limited text so design speaks to customer. I included our marketing line card to give some background on the company and what we offer.
Nice to have
• A kind of fade out of some sort or swoosh. Include colors from line card attached.
Should not have
• Mundane design.

```html
<!DOCTYPE html>
<html lang="en">
<head>
<meta charset="utf-8">
<title>Mobile Breeze and Volt – Stand-up Banner</title>
<link href="https://fonts.googleapis.com/css2?family=Archivo:wght@800&family=Montserrat:wght@500;600;700;800&family=Oswald:wght@400;600;700&display=swap" rel="stylesheet">
<style>
  :root{
    --bg:#7f7f7f;
    --white:#ffffff;
    --blue:#1456a4;
    --blue-light:#4f86c8;
    --red:#e8303d;
    --ink:#111111;
    --equip:#e6c832;
    --equip-dark:#6b6b5a;
  }
  *{margin:0;padding:0;box-sizing:border-box;}
  html,body{width:1200px;height:1200px;overflow:hidden;background:var(--bg);}
  .banner{
    position:absolute;left:350px;top:55px;width:500px;height:1090px;
    background:var(--white);box-shadow:0 6px 18px rgba(0,0,0,.35);overflow:hidden;
  }
  .banner-shapes{position:absolute;inset:0;}
  .brand{
    position:absolute;left:0;right:0;top:52px;display:flex;align-items:center;justify-content:center;gap:14px;
  }
  .brand-dot{width:82px;height:82px;border-radius:50%;background:var(--blue);flex:none;}
  .brand-name{
    font-family:"Montserrat",sans-serif;font-weight:700;color:var(--red);
    font-size:37px;line-height:1.02;
  }
  .offer-line{
    position:absolute;left:0;right:0;top:168px;text-align:center;
    font-family:"Archivo",sans-serif;font-weight:800;font-size:28px;color:var(--ink);letter-spacing:.2px;
  }
  .offer-line .sep{display:inline-block;width:12px;height:12px;border-radius:50%;background:var(--red);margin:0 12px;vertical-align:middle;position:relative;top:-2px;}
  .headline{
    position:absolute;left:0;right:0;top:296px;text-align:center;color:var(--white);
    font-family:"Oswald",sans-serif;font-weight:700;font-size:68px;line-height:1;letter-spacing:.5px;
  }
  .subhead{
    position:absolute;left:0;right:0;top:368px;text-align:center;color:var(--white);
    font-family:"Oswald",sans-serif;font-weight:400;font-size:29px;line-height:1.24;letter-spacing:.6px;
  }
  .summary{
    position:absolute;left:0;right:0;top:464px;text-align:center;color:var(--white);
    font-family:"Montserrat",sans-serif;font-weight:600;font-size:17px;line-height:1.3;
  }
  .section-tag{
    position:absolute;left:50%;top:588px;transform:translateX(-50%);
    background:var(--red);color:var(--white);border-radius:6px;padding:2px 14px 4px;
    font-family:"Montserrat",sans-serif;font-weight:700;font-size:24px;letter-spacing:.5px;
  }
  .service-list{
    position:absolute;top:655px;list-style:none;
    font-family:"Montserrat",sans-serif;font-weight:600;font-size:13.5px;color:var(--ink);text-transform:uppercase;line-height:1.18;
  }
  .service-list.left{left:30px;width:215px;}
  .service-list.right{left:262px;width:225px;}
  .service-list li{position:relative;padding-left:21px;margin-bottom:11px;}
  .service-list li::before{
    content:"";position:absolute;left:3px;top:0;width:6px;height:11px;
    border-right:3px solid var(--red);border-bottom:3px solid var(--red);transform:rotate(40deg);
  }
  .equipment{position:absolute;top:763px;width:122px;height:122px;}
  .equipment svg{position:absolute;inset:0;}
  .equipment .photo{
    position:absolute;left:22px;top:36px;width:78px;height:46px;border-radius:4px;
    background:linear-gradient(180deg,var(--equip) 0%,#cfae1e 60%,var(--equip-dark) 100%);
  }
  .eq-1{left:33px;} .eq-2{left:189px;} .eq-3{left:345px;}
  .rapid{
    position:absolute;left:0;right:0;top:924px;text-align:center;color:var(--white);
    font-family:"Montserrat",sans-serif;font-weight:800;font-size:19px;letter-spacing:2px;text-transform:uppercase;
  }
  .call{
    position:absolute;left:0;right:0;top:956px;text-align:center;color:var(--white);
    font-family:"Oswald",sans-serif;font-weight:600;font-size:46px;letter-spacing:.5px;line-height:1;
  }
  .web{
    position:absolute;left:50%;top:1026px;transform:translateX(-50%);
    background:var(--blue);color:var(--white);border-radius:9px;padding:6px 12px 8px;white-space:nowrap;
    font-family:"Montserrat",sans-serif;font-weight:500;font-size:19px;
  }
</style>
</head>
<body>
<main class="banner">
  <svg class="banner-shapes" width="500" height="1090" viewBox="0 0 500 1090" aria-hidden="true">
    <path d="M0,168 Q250,362 500,168 L500,628 Q250,478 0,628 Z" fill="var(--red)"/>
    <path d="M0,186 Q250,360 500,186 L500,610 Q250,482 0,610 Z" fill="var(--blue)"/>
    <rect x="0" y="911" width="500" height="179" fill="var(--red)"/>
  </svg>
  <svg class="banner-shapes" width="500" height="1090" viewBox="0 0 500 1090" role="img" aria-label="Faded background of HVAC equipment in a work area">
    <defs>
      <linearGradient id="equipment-fade" x1="0" y1="0" x2="0" y2="1">
        <stop offset="0" stop-color="var(--blue)" stop-opacity="0"/>
        <stop offset=".55" stop-color="var(--blue-light)" stop-opacity=".35"/>
        <stop offset="1" stop-color="var(--blue)" stop-opacity="0"/>
      </linearGradient>
    </defs>
    <path d="M0,186 Q250,360 500,186 L500,610 Q250,482 0,610 Z" fill="url(#equipment-fade)"/>
  </svg>

  <header class="brand">
    <span class="brand-dot"></span>
    <span class="brand-name">Mobile Breeze<br>and Volt</span>
  </header>
  <p class="offer-line">Rental<span class="sep"></span>Sales<span class="sep"></span>Service</p>

  <h1 class="headline">WE CAN POWER</h1>
  <p class="subhead">HEAT, OR COOL ANY FACILITY<br>OR EVENT YOU HAVE.</p>
  <p class="summary">Delivering rental generators, heating,<br>cooling, and chilling equipment of every size.</p>

  <span class="section-tag">Rental</span>
  <ul class="service-list left">
    <li>Air conditioner rental</li>
    <li>Generator rental</li>
    <li>Portable spot coolers rental &amp; power</li>
  </ul>
  <ul class="service-list right">
    <li>Chiller rental</li>
    <li>Breezer rental</li>
    <li>Portable heater rental</li>
  </ul>

  <div class="equipment eq-1">
    <svg viewBox="0 0 122 122" aria-hidden="true">
      <path d="M24,24 A52,52 0 0 1 113,61" fill="none" stroke="var(--blue)" stroke-width="6"/>
      <path d="M106,58 L120,58 L113,72 Z" fill="var(--blue)"/>
      <path d="M98,98 A52,52 0 0 1 9,61" fill="none" stroke="var(--red)" stroke-width="6"/>
      <path d="M2,64 L16,64 L9,50 Z" fill="var(--red)"/>
    </svg>
    <div class="photo" role="img" aria-label="Yellow trailer-mounted rental generator"></div>
  </div>
  <div class="equipment eq-2">
    <svg viewBox="0 0 122 122" aria-hidden="true">
      <path d="M24,24 A52,52 0 0 1 113,61" fill="none" stroke="var(--blue)" stroke-width="6"/>
      <path d="M106,58 L120,58 L113,72 Z" fill="var(--blue)"/>
      <path d="M98,98 A52,52 0 0 1 9,61" fill="none" stroke="var(--red)" stroke-width="6"/>
      <path d="M2,64 L16,64 L9,50 Z" fill="var(--red)"/>
    </svg>
    <div class="photo" role="img" aria-label="Yellow industrial chiller unit"></div>
  </div>
  <div class="equipment eq-3">
    <svg viewBox="0 0 122 122" aria-hidden="true">
      <path d="M24,24 A52,52 0 0 1 113,61" fill="none" stroke="var(--blue)" stroke-width="6"/>
      <path d="M106,58 L120,58 L113,72 Z" fill="var(--blue)"/>
      <path d="M98,98 A52,52 0 0 1 9,61" fill="none" stroke="var(--red)" stroke-width="6"/>
      <path d="M2,64 L16,64 L9,50 Z" fill="var(--red)"/>
    </svg>
    <div class="photo" role="img" aria-label="Yellow portable heater on trailer"></div>
  </div>

  <p class="rapid">24/7 Rapid Response</p>
  <p class="call">CALL: 1-888-417-2806</p>
  <p class="web">www.mobilebreezeandvolt.com</p>
</main>
</body>
</html>
```